Postcard Design

We need a postcard design for our 10 year anniversary open house. The company is Fernwood Medical Spa. The web site is www.fernwoodmedicalspa.com. We want royal blue, sliver and white colors for the postcard along with a 10 Year image.

It Company

```html
<!DOCTYPE html>
<html lang="en">
<head>
<meta charset="utf-8">
<title>Fernwood Medical Spa – 10th Anniversary Postcard</title>
<link href="https://fonts.googleapis.com/css2?family=Arimo:wght@400;700&family=Lobster+Two:ital,wght@1,700&family=Playfair+Display:ital@1&display=swap" rel="stylesheet">
<style>
  :root {
    --backdrop: #a3a2a3;
    --royal: #0a1fa8;
    --royal-deep: #0c1a9c;
    --royal-bright: #1536c8;
    --royal-band: #0b22b5;
    --white: #ffffff;
    --silver-1: #f2f2f4;
    --silver-2: #b9bbc2;
    --silver-3: #7d808a;
    --pink: #c9589f;
    --logo-blue: #2a4aa8;
    --stamp: #e5e5e8;
    --rule: #555a63;
    --text-light: #ffffff;
  }
  * { box-sizing: border-box; margin: 0; padding: 0; }
  html, body { width: 900px; height: 1200px; overflow: hidden; }
  body {
    background: var(--backdrop);
    position: relative;
    font-family: "Arimo", Arial, sans-serif;
  }
  .card {
    position: absolute;
    left: 109px;
    width: 684px;
    height: 440px;
    background: var(--white);
    box-shadow: 3px 4px 6px rgba(0,0,0,.45);
    overflow: hidden;
  }
  .card--front { top: 112px; }
  .card--back { top: 611px; height: 439px; }

  /* Front */
  .front-sidebar { position: absolute; left: 0; top: 0; width: 204px; height: 440px; }
  .sidebar-topband { position: absolute; left: 0; top: 0; width: 204px; height: 22px; background: var(--royal); }
  .logo-panel {
    position: absolute; left: 0; top: 22px; width: 222px; height: 104px;
    background: var(--white); z-index: 2;
    display: flex; flex-direction: column; align-items: center; justify-content: center; gap: 6px;
  }
  .logo-mark { width: 16px; height: 16px; border-radius: 50%; background: var(--logo-blue); }
  .logo-name { font-size: 19px; font-weight: 700; color: var(--logo-blue); letter-spacing: .5px; }
  .logo-sub { font-size: 9px; color: var(--logo-blue); text-align: center; line-height: 11px; }
  .tagline-band {
    position: absolute; left: 0; top: 126px; width: 204px; height: 85px;
    background: var(--royal-deep);
    display: flex; align-items: center; justify-content: center; text-align: center;
    font-family: "Lobster Two", cursive; font-style: italic; font-weight: 700;
    font-size: 12.5px; line-height: 17px; color: var(--text-light);
  }
  .invite-band {
    position: absolute; left: 0; top: 211px; width: 204px; height: 140px;
    background: linear-gradient(180deg, var(--royal-bright) 0%, var(--royal-band) 100%);
    color: var(--text-light); text-align: center;
  }
  .invite-line { position: absolute; left: 0; right: 0; top: 22px; font-size: 21px; }
  .invite-anniv {
    position: absolute; left: 0; right: 0; top: 58px;
    font-family: "Playfair Display", serif; font-style: italic; font-size: 19px;
  }
  .silver-band {
    position: absolute; left: 0; top: 335px; width: 204px; height: 105px;
    background: linear-gradient(180deg, var(--royal-band) 0%, var(--royal-band) 15%, var(--silver-1) 24%, var(--silver-2) 55%, var(--silver-3) 80%, var(--silver-2) 100%);
  }
  .hero-photo {
    position: absolute; left: 204px; top: 0; width: 480px; height: 440px;
    background: radial-gradient(circle at 30% 55%, #e7c2aa 0%, #d9ab93 28%, #f3ede8 55%, #ffffff 75%);
  }
  .hero-words {
    position: absolute; left: 419px; top: 10px;
    color: var(--pink); line-height: 1.05;
  }
  .hero-words span { display: block; }
  .hero-health, .hero-rejuvenate { font-size: 22px; }
  .hero-beauty { font-size: 31px; font-weight: 700; margin: 2px 0 3px; }

  /* Back */
  .back-photo {
    position: absolute; left: 0; top: 0; width: 361px; height: 191px;
    background: linear-gradient(160deg, #c69ad8 0%, #a66fc4 45%, #8c55b0 100%);
  }
  .back-info {
    position: absolute; left: 0; top: 191px; width: 361px; height: 248px;
    background: var(--royal); color: var(--text-light);
  }
  .info-heading {
    position: absolute; font-family: "Lobster Two", cursive; font-style: italic; font-weight: 700;
    font-size: 13px; padding-bottom: 1px; border-bottom: 1px solid var(--text-light);
  }
  .about-heading { left: 16px; top: 6px; width: 80px; }
  .about-text {
    position: absolute; left: 16px; top: 25px; width: 327px;
    font-size: 10px; line-height: 12.6px; text-align: justify;
  }
  .services-heading { left: 16px; top: 131px; width: 113px; }
  .contact-heading { left: 186px; top: 131px; width: 111px; }
  .info-divider { position: absolute; left: 163px; top: 137px; width: 1px; height: 80px; background: var(--text-light); }
  .service-list { position: absolute; left: 16px; top: 153px; list-style: none; font-size: 10px; line-height: 14px; }
  .service-list li::before { content: "\2713"; margin-right: 6px; }
  .contact-list { position: absolute; left: 183px; top: 153px; list-style: none; font-size: 10px; line-height: 12.5px; }
  .contact-list li { display: flex; gap: 6px; align-items: flex-start; }
  .contact-list svg { flex: 0 0 9px; margin-top: 2px; }
  .contact-list .indent { padding-left: 15px; }

  .stamp-box { position: absolute; left: 599px; top: 22px; width: 60px; height: 60px; background: var(--stamp); }
  .address-line { position: absolute; left: 406px; width: 258px; height: 1px; background: var(--rule); }
</style>
</head>
<body>

<section class="card card--front">
  <div class="front-sidebar">
    <div class="sidebar-topband"></div>
    <div class="logo-panel">
      <div class="logo-mark"></div>
      <div class="logo-name">Fernwood</div>
      <div class="logo-sub">Medical Spa<br>Cosmetic &amp; Laser Services</div>
    </div>
    <div class="tagline-band">All the Luxury You Deserve<br>with the Medical Expertise<br>You can Trust</div>
    <div class="invite-band">
      <div class="invite-line">Join Us for our</div>
      <div class="invite-anniv">10th Anniversary</div>
    </div>
    <div class="silver-band" role="img" aria-label="Sparkling silver glitter background with a royal blue ribbon bow and a jewel at its centre"></div>
  </div>
  <div class="hero-photo" role="img" aria-label="Photograph of a smiling woman with clear skin beside white and pink orchid flowers"></div>
  <div class="hero-words">
    <span class="hero-health">Health</span>
    <span class="hero-beauty">Beauty</span>
    <span class="hero-rejuvenate">Rejuvenate</span>
  </div>
</section>

<section class="card card--back">
  <div class="back-photo" role="img" aria-label="Photograph of lavender bath salts in a wooden bowl with a spoon and dried lavender sprigs on a purple surface"></div>
  <div class="back-info">
    <h2 class="info-heading about-heading">About Us:</h2>
    <p class="about-text">Finally after centuries of searching for rejuvenation, there is something that really works. Laser (light amplification by stimulated emition of radiation) proved itself not only helpful in medical/surgical field. Over the last 10 years it has become clear that low dose of laser stimulates collagen, removes signs of aging, photocoagulates unwanted vascular lesions and removes unwanted hair by photoepilation. Laser treatments in combination with Smoothera injections, Velane and Collagen fillers offer enormous boost to looks and self esteem.</p>

    <h2 class="info-heading services-heading">Our Services:</h2>
    <ul class="service-list">
      <li>Clarion</li>
      <li>Laser hair removal</li>
      <li>Dermatone pro 3layer</li>
      <li>Photo Facial</li>
      <li>Skin Rejuvenation</li>
    </ul>

    <div class="info-divider"></div>

    <h2 class="info-heading contact-heading">Contact Us:</h2>
    <ul class="contact-list">
      <li><svg width="9" height="11" viewBox="0 0 9 11"><path d="M4.5 0C2 0 0 2 0 4.4 0 7.5 4.5 11 4.5 11S9 7.5 9 4.4C9 2 7 0 4.5 0zm0 6.2a1.8 1.8 0 1 1 0-3.6 1.8 1.8 0 0 1 0 3.6z" fill="#fff"/></svg><span>1840 W. Alder Rd., Suite 210</span></li>
      <li class="indent">Reno, NV 89501</li>
      <li><svg width="9" height="9" viewBox="0 0 9 9"><path d="M2 0.5l1.4 1.9-.8 1c.5 1.2 1.5 2.2 2.8 2.8l1-.8L8.5 7 7.6 8.4C4 8.2.8 5 .6 1.4z" fill="#fff"/></svg><span>555.214.3380</span></li>
      <li><svg width="9" height="9" viewBox="0 0 9 9"><rect x="2" y="0.5" width="5" height="2.5" fill="#fff"/><rect x="0.5" y="3.5" width="8" height="3.5" rx="1" fill="#fff"/><rect x="2" y="6" width="5" height="2.5" fill="#fff"/></svg><span>555.214.6190</span></li>
    </ul>
  </div>

  <div class="stamp-box"></div>
  <div class="address-line" style="top:264px"></div>
  <div class="address-line" style="top:298px"></div>
  <div class="address-line" style="top:336px"></div>
</section>

</body>
</html>
```